Facebook Cover Photo & Mailchimp Template for Greyhound Racing Club

Create a consistent, professional visual identity across Facebook and email communications that promotes WTLB as a modern, community-focused greyhound racing club while respecting the heritage of greyhound racing.
Include WTLB logo.
Existing site https://www.pagelinkhub.net/MerrowfieldSprinters/

```html
<!DOCTYPE html>
<html lang="en">
<head>
<meta charset="utf-8">
<title>WTLB – Experience the Thrill</title>
<link href="https://fonts.googleapis.com/css2?family=Barlow+Condensed:wght@600&family=Barlow:wght@400;600;700&display=swap" rel="stylesheet">
<style>
  :root {
    --trees: #8a8456;
    --trees-deep: #5f6440;
    --grass: #9fb468;
    --crowd: #7d7a72;
    --rail: #f1efe9;
    --track-light: #b98e68;
    --track-mid: #9a7352;
    --track-dark: #5e412d;
    --sun: rgba(255, 230, 170, 0.7);
    --panel-green: rgba(38, 98, 48, 0.86);
    --panel-green-deep: rgba(26, 78, 36, 0.92);
    --ink-white: #ffffff;
    --ink-dark: #111111;
    --brand-black: #111111;
    --brand-green: #2f9a3a;
  }
  html, body {
    margin: 0;
    padding: 0;
    width: 1200px;
    height: 908px;
    overflow: hidden;
    background: #ffffff;
  }
  .cover {
    position: relative;
    width: 1200px;
    height: 908px;
    overflow: hidden;
    font-family: "Barlow", Arial, sans-serif;
  }
  .race-photo {
    position: absolute;
    inset: 0;
    background:
      radial-gradient(ellipse 520px 300px at 14% 0%, var(--sun), transparent 70%),
      linear-gradient(180deg,
        var(--trees) 0%,
        var(--trees-deep) 16%,
        var(--grass) 20%,
        var(--grass) 25%,
        var(--crowd) 27%,
        var(--crowd) 33%,
        var(--rail) 35%,
        #dcd6c8 39%,
        var(--grass) 42%,
        var(--grass) 46%,
        var(--track-light) 49%,
        var(--track-mid) 72%,
        var(--track-dark) 100%);
  }
  .info-panel {
    position: absolute;
    top: 0;
    right: 0;
    width: 450px;
    height: 908px;
    background: linear-gradient(180deg, var(--panel-green) 0%, var(--panel-green-deep) 100%);
  }
  .club-mark {
    position: absolute;
    left: 66px;
    top: 368px;
    display: flex;
    align-items: center;
    gap: 18px;
  }
  .club-mark__dot {
    width: 26px;
    height: 26px;
    border-radius: 50%;
    background: var(--brand-green);
  }
  .club-mark__name {
    font-family: "Barlow", Arial, sans-serif;
    font-weight: 700;
    font-size: 60px;
    line-height: 1;
    color: var(--brand-black);
    letter-spacing: 3px;
  }
  .headline {
    position: absolute;
    left: 786px;
    top: 388px;
    margin: 0;
    font-family: "Barlow Condensed", "Arial Narrow", sans-serif;
    font-weight: 600;
    font-size: 76px;
    line-height: 73px;
    color: var(--ink-white);
    letter-spacing: 1px;
    text-transform: uppercase;
  }
  .tagline {
    position: absolute;
    left: 794px;
    top: 544px;
    margin: 0;
    font-size: 27px;
    font-weight: 400;
    line-height: 1.2;
    color: var(--ink-white);
  }
  .join-button {
    position: absolute;
    left: 959px;
    top: 772px;
    width: 169px;
    height: 57px;
    display: flex;
    align-items: center;
    justify-content: center;
    background: var(--ink-white);
    color: var(--ink-dark);
    font-weight: 700;
    font-size: 23px;
    letter-spacing: 1px;
    text-decoration: none;
  }
</style>
</head>
<body>
  <main class="cover">
    <div class="race-photo" role="img" aria-label="Photo: greyhounds sprinting toward the camera on a sunlit dirt track, spectators behind the white rail"></div>
    <div class="info-panel"></div>
    <div class="club-mark">
      <span class="club-mark__dot"></span>
      <span class="club-mark__name">WTLB</span>
    </div>
    <h1 class="headline">Experience<br>the Thrill</h1>
    <p class="tagline">Community. Speed. Passion.</p>
    <a class="join-button" href="https://www.pagelinkhub.net/MerrowfieldSprinters/">JOIN US</a>
  </main>
</body>
</html>
```